Adapt a PowerPoint presentation to new Template

We have a new powerpoint template that we would like to adapt to our old powerpoint base presentation. I can share the old base template that is populated with information and data that needs to be adapted and "beautified" to the new template. I have all the source files necessary. Need to adapt the Lantern Harbor presentation to RWP Template. Meaning, to have the presentation look like the RWP template with no prior Lantern template scheme's (coloring, logos, font, etc)

Target Market(s)

Professionals

Requirements
Must have
• Adaption to our RWP Template
Nice to have
• Fully utilized tables, graphs, and graphics
Should not have
• Any Lantern Harbor Template palate

```html
<!DOCTYPE html>
<html lang="en"><head><meta charset="utf-8"><title>RWP Quarterly Review – Lantern Harbor</title>
<link href="https://fonts.googleapis.com/css2?family=Roboto:wght@400;500;700;900&display=swap" rel="stylesheet">
<style>
:root{--blue:#1b8cb8;--deep:#0f6c90;--teal:#2a9d8f;--ink:#1f2a35;--grey:#6b7682;--line:#dfe5ea;--bg:#ffffff;--neg:#f9d9de;--negt:#c8334a;--red:#b3202c}
*{box-sizing:border-box;margin:0;padding:0}
html,body{width:1200px;height:4515px;overflow:hidden;background:var(--bg);font-family:Roboto,Arial,sans-serif;color:var(--ink)}
.board{position:relative;width:1200px;height:4515px}
.hero{position:absolute;left:0;top:0;width:1200px;height:800px;background:#eef2f4;overflow:hidden}
.hero svg.bgshape{position:absolute;inset:0}
.hero .brand{position:absolute;right:80px;top:150px;font:900 44px Roboto,sans-serif;color:var(--ink);letter-spacing:1px}
.hero .hero-slide{left:170px;top:190px;transform:scale(1.38);transform-origin:0 0;box-shadow:0 20px 50px rgba(0,0,0,.25)}
.slide{position:absolute;width:561px;height:314px;background:#fff;overflow:hidden;box-shadow:0 1px 4px rgba(0,0,0,.12)}
.c1{left:26px}.c2{left:615px}
.pg{position:absolute;left:0;right:0;bottom:0;height:7px;background:var(--blue);font:500 5px Roboto,sans-serif;color:#fff;text-align:right;padding-right:12px;line-height:7px}
.mark{position:absolute;top:10px;right:14px;font:900 13px Roboto,sans-serif;color:var(--ink)}
.side{position:absolute;left:0;top:18px;bottom:7px;width:128px;background:var(--blue);border-radius:0 24px 0 0}
.nav{position:absolute;left:8px;top:62px;width:128px}
.nav div{height:34px;font:400 6.5px Roboto,sans-serif;color:#fff;padding:0 0 0 6px;display:flex;align-items:center}
.nav div.on{background:#fff;color:var(--blue);font-weight:700;border-radius:10px 0 0 10px;height:18px;margin:8px 0}
.ttl{position:absolute;left:150px;top:16px;font:700 19px Roboto,sans-serif;color:var(--blue)}
.fin{position:absolute;left:150px;top:62px;width:390px;font:400 5px Roboto,sans-serif;color:var(--grey)}
.fin .row{display:grid;grid-template-columns:102px repeat(6,48px);height:11.5px;align-items:center}
.fin .row span{text-align:right;padding-right:3px}
.fin .row span:first-child{text-align:right;padding-right:6px}
.fin .hd{height:14px;margin-bottom:4px}
.fin .hd b{grid-column:span 2;background:var(--blue);color:#fff;font-weight:700;text-align:center;border-radius:3px;margin:0 2px;line-height:11px}
.fin .sec span:first-child{text-align:left;color:var(--ink);font-weight:700}
.fin .tot span:first-child{color:var(--ink);font-weight:700}
.fin .n{background:var(--neg);color:var(--negt)}
.fin .net{background:var(--blue);color:#fff;border-radius:3px;margin-top:4px;font-weight:700}
.fin .net span{color:#fff}
.fin.one .row{grid-template-columns:102px repeat(2,48px)}
.ph{position:absolute}
.stitle{position:absolute;left:22px;top:16px;font:700 19px Roboto,sans-serif;color:var(--blue)}
.stitle em{font-style:normal;color:var(--deep)}
.sub{font:400 7px Roboto,sans-serif;color:var(--grey)}
.list{font:400 6.5px Roboto,sans-serif;color:var(--ink);line-height:14px}
.list b{font-weight:700}
.bbox{position:absolute;background:var(--blue);color:#fff;font:400 6px Roboto,sans-serif}
.bbox .k{font:400 6px Roboto,sans-serif;opacity:.85}
.bbox .v{font:700 13px Roboto,sans-serif}
.plan{position:absolute;left:320px;top:190px}
.plan li{list-style:none;display:flex;align-items:center;height:42px;font:700 8px Roboto,sans-serif;color:var(--ink)}
.plan li i{width:26px;height:26px;border-radius:50%;background:var(--blue);color:#fff;font:700 10px/26px Roboto,sans-serif;font-style:normal;text-align:center;margin-right:12px}
.plan li small{display:block;font:400 6px Roboto,sans-serif;color:var(--grey)}
.h2{position:absolute;font:700 21px/24px Roboto,sans-serif;color:var(--blue)}
.cf{position:absolute;left:22px;top:62px;width:520px;font:400 4.2px Roboto,sans-serif;color:var(--grey)}
.cf .row{display:grid;grid-template-columns:56px repeat(13,1fr);height:8px;align-items:center;text-align:right}
.cf .row span:first-child{text-align:left;color:var(--ink)}
.cf .bar{background:var(--blue);color:#fff}.cf .bar span{color:#fff}
</style></head>
<body><div class="board">

<section class="hero">
<svg class="bgshape" width="1200" height="800" viewBox="0 0 1200 800"><polygon points="0,0 420,0 0,330" fill="#1b8cb8"/><polygon points="0,470 1200,600 1200,800 0,800" fill="#1b8cb8"/><polygon points="0,580 700,800 0,800" fill="#0f6c90"/></svg>
<div class="brand">RWP</div>
<div class="slide hero-slide">
<div class="side"></div>
<div class="nav"><div class="on">Qtr. Actual vs Budget</div><div>Qtr. Actual vs Prior Year</div><div>YTD Actual vs. Budget</div><div>YTD Actual vs. Prior</div><div>YTD Actual vs. Projected Cash</div><div>Qtr. 3 - 21 Budget</div></div>
<div class="ttl">Qtr. Actual vs Budget</div><div class="mark">RWP</div>
<div class="fin">
<div class="row hd"><span></span><b>Actual</b><b>Budget</b><b>Variance $/%</b></div>
<div class="row sec"><span>Sales</span></div>
<div class="row tot"><span>Total Sales</span><span>$4,473,474</span><span>100.00%</span><span>$4,085,395</span><span>100.00%</span><span>$391,481</span><span>10.22%</span></div>
<div class="row sec"><span>Prime Cost</span></div>
<div class="row"><span>Cost of Goods</span><span>$1,275,661</span><span>28.44%</span><span>$1,075,820</span><span>26.77%</span><span class="n">($200,436)</span><span class="n">-18.67%</span></div>
<div class="row"><span>Personnel Costs</span><span>$1,344,276</span><span>30.05%</span><span>$1,068,236</span><span>26.68%</span><span class="n">($209,145)</span><span class="n">-20.81%</span></div>
<div class="row tot"><span>Total Prime Cost</span><span>$2,619,271</span><span>58.55%</span><span>$2,119,951</span><span>52.78%</span><span class="n">($499,058)</span><span class="n">-23.63%</span></div>
<div class="row sec"><span>Operating Expense</span></div>
<div class="row"><span>RCP</span><span>$1,760,764</span><span>39.17%</span><span>$1,365,221</span><span>34.18%</span><span>$346,540</span><span>25.34%</span></div>
<div class="row"><span>Total Operating Expense</span><span>$518,082</span><span>11.58%</span><span>$382,477</span><span>10.62%</span><span>($135,605)</span><span>-35.77%</span></div>
<div class="row sec"><span>Non Controllable Expense</span></div>
<div class="row"><span>Total Non-Controllable Expense</span><span>$775,093</span><span>17.18%</span><span>$712,469</span><span>14.78%</span><span>($61,624)</span><span>-8.60%</span></div>
<div class="row tot"><span>Total Field Contribution</span><span>$573,607</span><span>12.82%</span><span>$553,670</span><span>12.78%</span><span>$19,937</span><span>3.60%</span></div>
<div class="row"><span>Total Overhead</span><span>($23)</span><span>0.00%</span><span>$180,062</span><span>3.22%</span><span>$180,115</span><span>100.0%</span></div>
<div class="row net"><span>Net Profit</span><span>$574,709</span><span>12.80%</span><span>$372,348</span><span>9.16%</span><span>$202,361</span><span>54.32%</span></div>
</div>
<div class="pg">1</div>
</div>
</section>

<!-- Row 1 -->
<div class="slide c1" style="top:827px;background:var(--blue)">
<div style="position:absolute;left:0;right:0;top:140px;text-align:center;font:900 24px Roboto,sans-serif;color:#fff">RWP</div>
</div>
<div class="slide c2" style="top:827px">
<div style="position:absolute;left:52px;top:80px;font:700 11px Roboto,sans-serif;color:var(--red)">Lantern Harbor</div>
<div style="position:absolute;left:250px;top:78px;font:900 18px Roboto,sans-serif;color:var(--ink)">RWP</div>
<div style="position:absolute;left:52px;top:172px;font:500 22px Roboto,sans-serif;color:var(--blue)">LANTERN HARBOR, LLC</div>
<div style="position:absolute;left:52px;top:203px;font:400 10px Roboto,sans-serif;color:var(--grey)">Quarter 2, 2021</div>
<div class="ph" role="img" aria-label="Restaurant storefront exterior" style="right:0;top:0;width:200px;height:314px;background:linear-gradient(160deg,#c9d4dc,#8a9aa6);clip-path:polygon(35% 0,100% 0,100% 100%,0 100%)"></div>
<svg class="ph" style="right:0;top:0" width="240" height="314"><polygon points="90,0 160,0 60,314 0,314" fill="#1b8cb8" opacity=".85"/><polygon points="160,0 200,0 130,160" fill="#0f6c90" opacity=".8"/></svg>
</div>

<!-- Row 2 -->
<div class="slide c1" style="top:1156px">
<div class="side"></div>
<div class="nav"><div class="on">Qtr. Actual vs Budget</div><div>Qtr. Actual vs Prior Year</div><div>YTD Actual vs. Budget</div><div>YTD Actual vs. Prior</div><div>YTD Actual vs. Projected Cash</div><div>Qtr. 3 - 21 Budget</div></div>
<div class="ttl">Qtr. Actual vs Budget</div><div class="mark">RWP</div>
<div class="fin">
<div class="row hd"><span></span><b>Actual</b><b>Budget</b><b>Variance $/%</b></div>
<div class="row sec"><span>Sales</span></div>
<div class="row tot"><span>Total Sales</span><span>$4,473,474</span><span>100.00%</span><span>$4,085,395</span><span>100.00%</span><span>$391,481</span><span>10.22%</span></div>
<div class="row sec"><span>Prime Cost</span></div>
<div class="row"><span>Cost of Goods</span><span>$1,275,661</span><span>28.44%</span><span>$1,075,820</span><span>26.77%</span><span class="n">($200,436)</span><span class="n">-18.67%</span></div>
<div class="row"><span>Personnel Costs</span><span>$1,344,276</span><span>30.05%</span><span>$1,068,236</span><span>26.68%</span><span class="n">($209,145)</span><span class="n">-20.81%</span></div>
<div class="row tot"><span>Total Prime Cost</span><span>$2,619,271</span><span>58.55%</span><span>$2,119,951</span><span>52.78%</span><span class="n">($499,058)</span><span class="n">-23.63%</span></div>
<div class="row sec"><span>Operating Expense</span></div>
<div class="row"><span>RCP</span><span>$1,760,764</span><span>39.17%</span><span>$1,365,221</span><span>34.18%</span><span>$346,540</span><span>25.34%</span></div>
<div class="row"><span>Total Operating Expense</span><span>$518,082</span><span>11.58%</span><span>$382,477</span><span>10.62%</span><span>($135,605)</span><span>-35.77%</span></div>
<div class="row sec"><span>Non Controllable Expense</span></div>
<div class="row"><span>Total Non-Controllable Expense</span><span>$775,093</span><span>17.18%</span><span>$712,469</span><span>14.78%</span><span>($61,624)</span><span>-8.60%</span></div>
<div class="row tot"><span>Total Field Contribution</span><span>$573,607</span><span>12.82%</span><span>$553,670</span><span>12.78%</span><span>$19,937</span><span>3.60%</span></div>
<div class="row"><span>Total Overhead</span><span>($23)</span><span>0.00%</span><span>$180,062</span><span>3.22%</span><span>$180,115</span><span>100.0%</span></div>
<div class="row net"><span>Net Profit</span><span>$574,709</span><span>12.80%</span><span>$372,348</span><span>9.16%</span><span>$202,361</span><span>54.32%</span></div>
</div><div class="pg">3</div></div>

<div class="slide c2" style="top:1156px">
<div class="side"></div>
<div class="nav"><div>Qtr. Actual vs Budget</div><div class="on">Qtr. Actual vs Prior Year</div><div>YTD Actual vs. Budget</div><div>YTD Actual vs. Prior</div><div>YTD Actual vs. Projected Cash</div><div>Qtr. 3 - 21 Budget</div></div>
<div class="ttl">Qtr. Actual vs Prior Year</div><div class="mark">RWP</div>
<div class="fin">
<div class="row hd"><span></span><b>Actual</b><b>Prior Year</b><b>Variance $/%</b></div>
<div class="row sec"><span>Sales</span></div>
<div class="row tot"><span>Total Sales</span><span>$4,473,474</span><span>100.00%</span><span>$3,880,253</span><span>100.00%</span><span>$593,221</span><span>15.29%</span></div>
<div class="row sec"><span>Prime Cost</span></div>
<div class="row"><span>Cost of Goods</span><span>$1,275,661</span><span>28.44%</span><span>$905,508</span><span>23.33%</span><span class="n">($370,153)</span><span class="n">-40.88%</span></div>
<div class="row"><span>Personnel Costs</span><span>$1,344,276</span><span>30.05%</span><span>$1,014,526</span><span>26.14%</span><span class="n">($329,750)</span><span class="n">-32.50%</span></div>
<div class="row tot"><span>Total Prime Cost</span><span>$2,619,271</span><span>58.55%</span><span>$1,919,384</span><span>49.47%</span><span class="n">($699,887)</span><span class="n">-36.46%</span></div>
<div class="row sec"><span>Operating Expense</span></div>
<div class="row"><span>RCP</span><span>$1,760,764</span><span>39.17%</span><span>$1,058,660</span><span>34.38%</span><span>$608,520</span><span>61.48%</span></div>
<div class="row"><span>Total Operating Expense</span><span>$518,082</span><span>11.58%</span><span>$408,718</span><span>10.53%</span><span>($109,364)</span><span>-26.76%</span></div>
<div class="row sec"><span>Non Controllable Expense</span></div>
<div class="row"><span>Total Non-Controllable Expense</span><span>$775,093</span><span>17.18%</span><span>$580,463</span><span>14.96%</span><span>($194,630)</span><span>-33.53%</span></div>
<div class="row tot"><span>Total Field Contribution</span><span>$573,607</span><span>12.82%</span><span>$175,001</span><span>4.51%</span><span>$398,606</span><span>227.8%</span></div>
<div class="row"><span>Total Overhead</span><span>($23)</span><span>0.00%</span><span>$122,519</span><span>3.16%</span><span>$122,542</span><span>100.0%</span></div>
<div class="row net"><span>Net Profit</span><span>$574,709</span><span>12.80%</span><span>$52,482</span><span>1.35%</span><span>$522,227</span><span>995.0%</span></div>
</div><div class="pg">4</div></div>

<!-- Row 3 -->
<div class="slide c1" style="top:1486px">
<div class="side"></div>
<div class="nav"><div>Qtr. Actual vs Budget</div><div>Qtr. Actual vs Prior Year</div><div class="on">YTD Actual vs. Budget</div><div>YTD Actual vs. Prior</div><div>YTD Actual vs. Projected Cash</div><div>Qtr. 3 - 21 Budget</div></div>
<div class="ttl">YTD Actual vs. Budget</div><div class="mark">RWP</div>
<div class="fin">
<div class="row hd"><span></span><b>YTD Actual</b><b>YTD Budget</b><b>Variance $/%</b></div>
<div class="row sec"><span>Sales</span></div>
<div class="row tot"><span>Total Sales</span><span>$4,473,474</span><span>100.00%</span><span>$3,880,253</span><span>100.00%</span><span>$1,799,148</span><span>16.42%</span></div>
<div class="row sec"><span>Prime Cost</span></div>
<div class="row"><span>Cost of Goods</span><span>$1,275,661</span><span>28.44%</span><span>$905,508</span><span>23.33%</span><span class="n">($370,153)</span><span class="n">-40.88%</span></div>
<div class="row"><span>Personnel Costs</span><span>$1,344,276</span><span>30.05%</span><span>$1,014,526</span><span>26.14%</span><span class="n">($329,750)</span><span class="n">-32.50%</span></div>
<div class="row tot"><span>Total Prime Cost</span><span>$2,619,271</span><span>58.55%</span><span>$1,919,384</span><span>49.47%</span><span class="n">($699,887)</span><span class="n">-36.46%</span></div>
<div class="row sec"><span>Operating Expense</span></div>
<div class="row"><span>RCP</span><span>$1,760,764</span><span>39.17%</span><span>$1,058,660</span><span>34.38%</span><span>$608,520</span><span>61.48%</span></div>
<div class="row"><span>Total Operating Expense</span><span>$518,082</span><span>11.58%</span><span>$408,718</span><span>10.53%</span><span>($117,573)</span><span>-26.76%</span></div>
<div class="row sec"><span>Non Controllable Expense</span></div>
<div class="row"><span>Total Non-Controllable Expense</span><span>$775,093</span><span>17.18%</span><span>$580,463</span><span>14.96%</span><span>($190,602)</span><span>-32.67%</span></div>
<div class="row tot"><span>Total Field Contribution</span><span>$573,607</span><span>12.82%</span><span>$175,001</span><span>4.51%</span><span>$398,606</span><span>227.8%</span></div>
<div class="row"><span>Total Overhead</span><span>($23)</span><span>0.00%</span><span>$122,519</span><span>3.16%</span><span>$122,542</span><span>100.0%</span></div>
<div class="row net"><span>Net Profit</span><span>$574,709</span><span>12.80%</span><span>$52,482</span><span>1.35%</span><span>$522,227</span><span>995.0%</span></div>
</div><div class="pg">5</div></div>

<div class="slide c2" style="top:1486px">
<div class="side"></div>
<div class="nav"><div>Qtr. Actual vs Budget</div><div>Qtr. Actual vs Prior Year</div><div>YTD Actual vs. Budget</div><div class="on">YTD Actual vs. Prior</div><div>YTD Actual vs. Projected Cash</div><div>Qtr. 3 - 21 Budget</div></div>
<div class="ttl">YTD Actual vs. Prior</div><div class="mark">RWP</div>
<div class="fin">
<div class="row hd"><span></span><b>YTD Actual</b><b>YTD Prior</b><b>Variance $/%</b></div>
<div class="row sec"><span>Sales</span></div>
<div class="row tot"><span>Total Sales</span><span>$4,473,474</span><span>100.00%</span><span>$3,880,253</span><span>100.00%</span><span>$1,799,148</span><span>16.42%</span></div>
<div class="row sec"><span>Prime Cost</span></div>
<div class="row"><span>Cost of Goods</span><span>$1,275,661</span><span>28.44%</span><span>$905,508</span><span>23.33%</span><span class="n">($370,153)</span><span class="n">-40.88%</span></div>
<div class="row"><span>Personnel Costs</span><span>$1,344,276</span><span>30.05%</span><span>$1,014,526</span><span>26.14%</span><span class="n">($329,750)</span><span class="n">-32.50%</span></div>
<div class="row tot"><span>Total Prime Cost</span><span>$2,619,271</span><span>58.55%</span><span>$1,919,384</span><span>49.47%</span><span class="n">($699,887)</span><span class="n">-36.46%</span></div>
<div class="row sec"><span>Operating Expense</span></div>
<div class="row"><span>RCP</span><span>$1,760,764</span><span>39.17%</span><span>$1,058,660</span><span>34.38%</span><span>$608,520</span><span>61.48%</span></div>
<div class="row"><span>Total Operating Expense</span><span>$518,082</span><span>11.58%</span><span>$408,718</span><span>10.53%</span><span>($117,573)</span><span>-26.76%</span></div>
<div class="row sec"><span>Non Controllable Expense</span></div>
<div class="row"><span>Total Non-Controllable Expense</span><span>$775,093</span><span>17.18%</span><span>$580,463</span><span>14.96%</span><span>($190,602)</span><span>-32.67%</span></div>
<div class="row tot"><span>Total Field Contribution</span><span>$573,607</span><span>12.82%</span><span>$175,001</span><span>4.51%</span><span>$398,606</span><span>227.8%</span></div>
<div class="row"><span>Total Overhead</span><span>($23)</span><span>0.00%</span><span>$122,519</span><span>3.16%</span><span>$122,542</span><span>100.0%</span></div>
<div class="row net"><span>Net Profit</span><span>$574,709</span><span>12.80%</span><span>$52,482</span><span>1.35%</span><span>$522,227</span><span>995.0%</span></div>
</div><div class="pg">6</div></div>

<!-- Row 4 -->
<div class="slide c1" style="top:1810px">
<div class="side"></div>
<div class="nav"><div>Qtr. Actual vs Budget</div><div>Qtr. Actual vs Prior Year</div><div>YTD Actual vs. Budget</div><div>YTD Actual vs. Prior</div><div class="on">YTD Actual vs. Projected Cash</div><div>Qtr. 3 - 21 Budget</div></div>
<div class="ttl">YTD Actual vs. Projected Cash</div><div class="mark">RWP</div>
<svg style="position:absolute;left:150px;top:56px" width="395" height="240" viewBox="0 0 395 240" font-family="Roboto,sans-serif" font-size="5" fill="#6b7682">
<g stroke="#e4e9ed" stroke-width=".6"><line x1="40" y1="30" x2="385" y2="30"/><line x1="40" y1="62" x2="385" y2="62"/><line x1="40" y1="94" x2="385" y2="94"/><line x1="40" y1="126" x2="385" y2="126"/><line x1="40" y1="158" x2="385" y2="158"/><line x1="40" y1="190" x2="385" y2="190"/></g>
<text x="8" y="32">$1,600,000</text><text x="8" y="64">$1,400,000</text><text x="8" y="96">$1,200,000</text><text x="8" y="128">$1,000,000</text><text x="8" y="160">$800,000</text><text x="8" y="192">$600,000</text>
<polyline points="50,140 95,165 140,130 185,150 230,140 275,120 320,80 370,30" fill="none" stroke="#1b8cb8" stroke-width="1.6"/>
<polyline points="50,150 95,170 140,145 185,160 230,150 275,140 320,110 370,135" fill="none" stroke="#2a9d8f" stroke-width="1.2"/>
<rect x="300" y="10" width="60" height="14" rx="2" fill="#1f2a35"/><text x="306" y="19" fill="#fff" font-size="5.5" font-weight="700">Replace your</text>
<text x="48" y="200">P1</text><text x="93" y="200">P2</text><text x="138" y="200">P3</text><text x="183" y="200">P4</text><text x="228" y="200">P5</text><text x="273" y="200">P6</text><text x="318" y="200">P7</text>
<text x="8" y="212">Cash Projection</text><text x="8" y="222">Cash Balance</text>
<text x="48" y="212">$1,103,218</text><text x="93" y="212">$1,041,206</text><text x="138" y="212">$1,187,665</text><text x="183" y="212">$1,093,183</text><text x="228" y="212">$1,160,311</text><text x="273" y="212">$1,259,110</text><text x="318" y="212">$1,501,889</text>
<text x="48" y="222">$1,018,756</text><text x="93" y="222">$961,273</text><text x="138" y="222">$1,104,588</text><text x="183" y="222">$1,053,622</text><text x="228" y="222">$1,094,361</text><text x="273" y="222">$1,198,055</text><text x="318" y="222">$1,371,416</text>
</svg><div class="pg">7</div></div>

<div class="slide c2" style="top:1810px">
<div class="side"></div>
<div class="nav"><div>Qtr. Actual vs Budget</div><div>Qtr. Actual vs Prior Year</div><div>YTD Actual vs. Budget</div><div>YTD Actual vs. Prior</div><div>YTD Actual vs. Projected Cash</div><div class="on">Qtr. 3 - 21 Budget</div></div>
<div class="ttl">Qtr. 3 - 21 Budget</div><div class="mark">RWP</div>
<div class="fin one" style="left:190px">
<div class="row hd"><span></span><b>Budget</b></div>
<div class="row sec"><span>Sales</span></div>
<div class="row tot"><span>Total Sales</span><span>$4,473,474</span><span>100.00%</span></div>
<div class="row sec"><span>Prime Cost</span></div>
<div class="row"><span>Cost of Goods</span><span>$1,275,661</span><span>28.44%</span></div>
<div class="row"><span>Personnel Costs</span><span>$1,344,276</span><span>30.05%</span></div>
<div class="row tot"><span>Total Prime Cost</span><span>$2,619,271</span><span>58.55%</span></div>
<div class="row sec"><span>Operating Expense</span></div>
<div class="row"><span>RCP</span><span>$1,760,764</span><span>39.17%</span></div>
<div class="row"><span>Total Operating Expense</span><span>$518,082</span><span>11.58%</span></div>
<div class="row sec"><span>Non Controllable Expense</span></div>
<div class="row"><span>Total Non-Controllable Expense</span><span>$775,093</span><span>17.18%</span></div>
<div class="row tot"><span>Total Field Contribution</span><span>$573,607</span><span>12.82%</span></div>
<div class="row"><span>Total Overhead</span><span>($23)</span><span>0.00%</span></div>
<div class="row net"><span>Net Profit</span><span>$574,709</span><span>12.80%</span></div>
</div><div class="pg">8</div></div>

<!-- Row 5 -->
<div class="slide c1" style="top:2148px">
<div class="stitle"><em>Go Forward</em> Step Plan</div><div class="mark">RWP</div>
<svg style="position:absolute;left:80px;top:62px" width="36" height="36"><circle cx="18" cy="18" r="16" fill="none" stroke="#1b8cb8" stroke-width="1.5"/><circle cx="18" cy="14" r="4" fill="#1b8cb8"/><path d="M10 26c2-5 14-5 16 0" fill="none" stroke="#1b8cb8" stroke-width="2"/></svg>
<svg style="position:absolute;left:372px;top:62px" width="36" height="36"><circle cx="18" cy="18" r="16" fill="none" stroke="#1b8cb8" stroke-width="1.5"/><path d="M11 18a7 7 0 0 1 12-5M25 18a7 7 0 0 1-12 5" fill="none" stroke="#1b8cb8" stroke-width="2"/><path d="M23 9v4h-4M13 27v-4h4" fill="none" stroke="#1b8cb8" stroke-width="1.6"/></svg>
<div style="position:absolute;left:60px;top:112px;font:700 7px Roboto,sans-serif;color:var(--blue)">RWP Support Team</div>
<div class="list" style="position:absolute;left:60px;top:124px">•• <b>Evan Marsh</b> / CEO<br>•• <b>Neil Porter</b> / COO<br>•• <b>Rita Collins</b> / Controller<br>•• <b>Joanna Reyes</b> / Human Relations<br>•• <b>Cole Bennett</b> / Operations Services Manager</div>
<div style="position:absolute;left:355px;top:112px;font:700 7px Roboto,sans-serif;color:var(--blue)">Key Focus Items</div>
<div class="list" style="position:absolute;left:320px;top:124px;width:170px;line-height:10px">•• Bench building process followed for people growth<br><br>•• Review CapX projects for year end<br><br>•• Prepare NRO management team for Sandhill and Falcon</div>
<div class="pg">9</div></div>

<div class="slide c2" style="top:2148px">
<div class="stitle"><em>Go Forward</em> Step Plan</div><div class="mark">RWP</div>
<div class="sub" style="position:absolute;left:22px;top:44px;font-weight:700;color:var(--blue)">RWP Support Team</div>
<div class="ph" role="img" aria-label="Portrait of the CEO" style="left:22px;top:70px;width:38px;height:38px;background:linear-gradient(#9fb3c1,#5f7686)"></div>
<div class="ph" role="img" aria-label="Portrait of the COO" style="left:22px;top:120px;width:38px;height:38px;background:linear-gradient(#1b8cb8,#0f6c90)"></div>
<div class="ph" role="img" aria-label="Portrait of the controller" style="left:22px;top:170px;width:38px;height:38px;background:linear-gradient(#c9b7a8,#8b7464)"></div>
<div class="ph" role="img" aria-label="Portrait of the HR lead" style="left:190px;top:70px;width:38px;height:38px;background:linear-gradient(#d2b9a5,#8f6e58)"></div>
<div class="ph" role="img" aria-label="Portrait of the operations manager" style="left:190px;top:120px;width:38px;height:38px;background:linear-gradient(#1b8cb8,#0f6c90)"></div>
<div class="list" style="position:absolute;left:68px;top:76px;line-height:8px"><b style="color:var(--blue)">Evan Marsh</b><br><span class="sub">CEO</span></div>
<div class="list" style="position:absolute;left:68px;top:126px;line-height:8px"><b style="color:var(--blue)">Neil Porter</b><br><span class="sub">COO</span></div>
<div class="list" style="position:absolute;left:68px;top:176px;line-height:8px"><b style="color:var(--blue)">Rita Collins</b><br><span class="sub">Controller</span></div>
<div class="list" style="position:absolute;left:236px;top:76px;line-height:8px"><b style="color:var(--blue)">Joanna Reyes</b><br><span class="sub">Human Relations</span></div>
<div class="list" style="position:absolute;left:236px;top:126px;line-height:8px"><b style="color:var(--blue)">Cole Bennett</b><br><span class="sub">Operations Services<br>Manager</span></div>
<div class="bbox" style="left:370px;top:60px;width:191px;height:200px;padding:24px 18px;border-radius:16px 0 0 16px">
<div style="font:700 8px Roboto,sans-serif;text-align:center;margin-bottom:14px">Key Focus Items</div>
<div style="line-height:10px">•• Bench building process followed for people growth<br><br>•• Review CapX projects for year end<br><br>•• Prepare NRO management team for Sandhill and Falcon</div></div>
<div class="pg">10</div></div>

<!-- Row 6 -->
<div class="slide c1" style="top:2476px">
<div class="stitle">2021 Updated Cash Flow Model</div><div class="mark">RWP</div>
<div class="cf">
<div class="row bar"><span></span><span>P1 2021</span><span>P2 2021</span><span>P3 2021</span><span>P4 2021</span><span>P5 2021</span><span>P6 2021</span><span>P7 2021</span><span>P8 2021</span><span>P9 2021</span><span>P10 2021</span><span>P11 2021</span><span>P12 2021</span><span>P13 2021</span></div>
<div class="row"><span>Cash, Beginning of Period</span><span>$1,023,167</span><span>$1,256,392</span><span>$1,218,445</span><span>$1,404,611</span><span>$1,337,815</span><span>$1,418,231</span><span>$1,218,330</span><span>$1,378,237</span><span>$1,601,173</span><span>$1,512</span><span>$1,498</span><span>$1,522</span><span>$1,560</span></div>
<div class="row"><span>Cash Flow Non-Operations</span><span>$368,674</span><span>$35,308</span><span>$156,525</span><span>$80,837</span><span>$88,337</span><span>$174,334</span><span>$172,786</span><span>$176,387</span><span>$184,331</span><span>$88</span><span>$90</span><span>$92</span><span>$95</span></div>
<div class="row"><span>Cap Ex &amp; Other</span><span></span><span></span><span></span><span></span><span></span><span></span><span></span><span>$29,668</span><span>$36,000</span><span>$30,000</span><span>$30,000</span><span>$30,000</span><span>$30,000</span></div>
<div class="row"><span>Sand Hill Development</span><span></span><span></span><span></span><span></span><span></span><span></span><span></span><span>$26,000</span><span>$25,000</span><span>$25,000</span><span>$50,000</span><span>$50,000</span><span>$50,000</span></div>
<div class="row"><span>Falcon Development</span><span></span><span></span><span></span><span></span><span></span><span></span><span></span><span>$16,000</span><span>$15,000</span><span>$20,000</span><span>$30,000</span><span>$30,000</span><span>$30,000</span></div>
<div class="row"><span></span><span style="grid-column:span 6;background:var(--blue);color:#fff;text-align:center;border-radius:2px">Model excludes PPP &amp; ERC</span></div>
<div class="row"><span></span></div>
<div class="row"><span>Debt Payments</span></div>
<div class="row"><span>PL Port Finance</span><span>$545</span><span>$545</span><span>$545</span><span>$545</span><span>$545</span><span>$545</span><span>$545</span><span>$545</span><span>$545</span><span>$545</span><span>$545</span><span>$545</span><span>$545</span></div>
<div class="row"><span>Equip. Loan A</span><span>$164</span><span>$164</span><span>$164</span><span>$164</span><span>$164</span><span>$164</span><span>$164</span><span>$164</span><span>$164</span><span>$164</span><span>$164</span><span>$164</span><span>$164</span></div>
<div class="row"><span>Equip. Loan B</span><span>$1,258</span><span>$1,258</span><span>$1,258</span><span>$1,258</span><span>$1,258</span><span>$1,258</span><span>$1,258</span><span>$1,258</span><span>$1,258</span><span>$1,258</span><span>$1,258</span><span>$1,258</span><span>$1,258</span></div>
<div class="row"><span>Senior Note</span><span>$3,640</span><span>$3,640</span><span>$3,640</span><span>$3,640</span><span>$3,640</span><span>$3,640</span><span>$3,640</span><span>$3,640</span><span>$3,640</span><span>$3,640</span><span>$3,640</span><span>$3,640</span><span>$3,640</span></div>
<div class="row"><span>Term Loan</span><span>$2,750</span><span>$2,750</span><span>$2,750</span><span>$2,750</span><span>$2,750</span><span>$2,750</span><span>$2,750</span><span>$2,750</span><span>$2,750</span><span>$2,750</span><span>$2,750</span><span>$2,750</span><span>$2,750</span></div>
<div class="row"><span>Line Interest</span><span>$900</span><span>$900</span><span>$900</span><span>$900</span><span>$900</span><span>$900</span><span>$900</span><span>$900</span><span>$900</span><span>$900</span><span>$900</span><span>$900</span><span>$900</span></div>
<div class="row"><span>Lease Note</span><span>$100,190</span><span>$100,190</span><span>$100,190</span><span>$100,190</span><span>$100,190</span><span>$100,190</span><span>$100,190</span><span>$40,000</span><span>$40,000</span><span>$40,000</span><span>$40,000</span><span>$40,000</span><span>$40,000</span></div>
<div class="row"><span>Other</span><span>$89</span><span>$89</span><span>$89</span><span>$89</span><span>$89</span><span>$89</span><span>$89</span><span>$89</span><span>$89</span><span>$89</span><span>$89</span><span>$89</span><span>$89</span></div>
<div class="row"><span></span></div><div class="row"><span></span></div><div class="row"><span></span></div>
<div class="row bar"><span>Cash, End of Period</span><span>$0</span><span>$0</span><span>$0</span><span>$1,320,961</span><span>$1,255,393</span><span>$1,173,643</span><span>$1,374,618</span><span>$1,217,233</span><span>$1,183,003</span><span>$1,512</span><span>$1,498</span><span>$1,522</span><span>$1,560</span></div>
</div><div class="pg">11</div></div>

<div class="slide c2" style="top:2476px">
<div class="mark" style="left:22px;right:auto">RWP</div>
<div class="h2" style="left:50px;top:62px">Current Cash<br>Holding</div>
<div class="sub" style="position:absolute;left:50px;top:118px">Current Cash as of 8/25/21</div>
<div class="ph" role="img" aria-label="Smiling restaurant team member holding a burger basket" style="left:240px;top:0;width:321px;height:314px;background:linear-gradient(135deg,#c46a4a,#7a2b25 60%,#3b2a2a);clip-path:polygon(30% 0,100% 0,100% 100%,0 100%)"></div>
<svg class="ph" style="left:230px;top:0" width="200" height="314"><polygon points="95,0 140,0 40,190 0,190" fill="#1b8cb8" opacity=".85"/></svg>
<div class="bbox" style="left:50px;top:145px;width:260px;height:120px;padding:14px 14px">
<div style="display:grid;grid-template-columns:1fr 1fr;row-gap:12px">
<div><div class="k">Harbor Trust</div><div class="v">$1,532,893</div><div class="k">Checking</div></div>
<div><div class="k">Plains Western Bank</div><div class="v" style="font-size:11px">$931,358 &nbsp;$99,934</div><div class="k">Money Market &nbsp; RWP DC Checking</div></div>
<div><div class="k">Total cash</div><div class="v">$2,564,190</div></div>
<div><div class="k">3430 ERC credit</div><div class="v">$1,053,536</div><div class="k">Anticipated deposit Q1-22</div></div>
</div></div>
<div class="sub" style="position:absolute;left:150px;top:272px;font-size:5px">*2021 ERC under review</div>
<div class="pg">12</div></div>

<!-- Row 7 -->
<div class="slide c1" style="top:2808px">
<div class="mark" style="left:22px;right:auto">RWP</div>
<div class="h2" style="left:40px;top:88px">Calloway</div>
<div class="sub" style="position:absolute;left:40px;top:118px">At PSA/Phase to Sell</div>
<div class="ph" role="img" aria-label="Burger restaurant exterior with red striped awning" style="left:220px;top:0;width:341px;height:314px;background:linear-gradient(180deg,#a9c3db 0%,#c9d7e2 40%,#b4343a 55%,#6e6a66 80%,#8d8a86);clip-path:polygon(40% 0,100% 0,100% 100%,0 100%)"></div>
<div class="bbox" style="left:0;top:150px;width:290px;height:48px;padding:8px 40px;display:flex;gap:40px">
<div><div class="k">Sales price</div><div class="v">$1.1M</div></div>
<div><div class="k">Current debt</div><div class="v">$89k</div></div>
<div><div class="k">Target date</div><div class="v">10/06/21</div></div></div>
<div class="sub" style="position:absolute;left:40px;top:210px;font-size:6px">Approved by Bramble's Corp</div>
<div class="pg">13</div></div>

<div class="slide c2" style="top:2808px">
<div class="mark" style="left:22px;right:auto">RWP</div>
<div class="h2" style="left:22px;top:30px">Sand Hill</div>
<div class="sub" style="position:absolute;left:22px;top:56px;color:var(--blue);font-size:8px">Colorado Springs, CO</div>
<div class="sub" style="position:absolute;left:22px;top:76px;font-size:5.5px">2,600 sqft End-Cap with Drive-Thru</div>
<div class="bbox" style="left:22px;top:100px;width:200px;height:170px;padding:12px 14px;display:grid;grid-template-columns:1fr 1fr;row-gap:10px">
<div><div class="k">Total project est</div><div class="v">$950k</div></div>
<div><div class="k">Funded debt</div><div class="v">$635k</div></div>
<div><div class="k">Equity</div><div class="v">$160k</div></div>
<div><div class="k">Soft cost cash</div><div class="v">$155k</div></div>
<div><div class="k">Annual return</div><div class="v">$99k</div></div>
<div><div class="k">Projected opening</div><div class="v">Qtr. 2, 2022</div></div></div>
<div class="ph" role="img" aria-label="Site plan map of the Sand Hill retail center" style="left:240px;top:20px;width:305px;height:270px;background:linear-gradient(135deg,#d6c8d2,#9b8a98 60%,#6f6a70)"></div>
<div class="pg">14</div></div>

<!-- Row 8 -->
<div class="slide c1" style="top:3138px">
<div class="mark">RWP</div>
<div class="ph" role="img" aria-label="Technical site drawing of the Falcon property" style="left:20px;top:20px;width:230px;height:230px;background:linear-gradient(135deg,#f1f3f6,#d9dee4)"></div>
<div class="sub" style="position:absolute;left:95px;top:262px">Projected opening Qtr. 3, 2022</div>
<div class="h2" style="left:270px;top:30px">Falcon</div>
<div class="sub" style="position:absolute;left:270px;top:56px;color:var(--blue);font-size:8px">Falcon, CO</div>
<div class="sub" style="position:absolute;left:270px;top:72px;font-size:5.5px">PSA to acquire .75 acre &amp; construct 3030 sqft bldg</div>
<div class="list" style="position:absolute;left:270px;top:88px;width:260px;font-size:5.5px;line-height:9px">
<div style="display:grid;grid-template-columns:1fr 1fr;gap:8px">
<div><div style="background:var(--blue);color:#fff;padding:0 4px">Real Estate</div>Total investment <b style="float:right">$1.025M</b><br>Purchase Price <b style="float:right">$1M</b><br>Soft Cost <b style="float:right">$25k</b><br>Funded Debt <b style="float:right">$800k</b><br>Equity <b style="float:right">$200k</b></div>
<div><div style="background:var(--blue);color:#fff;padding:0 4px">Bramble's</div>Total investment <b style="float:right">$1.1M</b><br>Funded Debt <b style="float:right">$788k</b><br>Equity <b style="float:right">$188k</b><br>Soft Cost <b style="float:right">$157k</b></div>
<div><div style="background:var(--blue);color:#fff;padding:0 4px">RE Development</div>Total investment <b style="float:right">$500</b><br>Funded Debt <b style="float:right">$400k</b><br>Equity <b style="float:right">$100k</b></div>
</div></div>
<div class="pg">15</div></div>

<div class="slide c2" style="top:3138px">
<div class="mark">RWP</div>
<div class="ph" role="img" aria-label="Map of Colorado development sites" style="left:0;top:0;width:300px;height:307px;background:linear-gradient(160deg,#e8ece4,#cfd9cf 60%,#bcc8d3)"></div>
<div class="h2" style="left:320px;top:70px">Colorado<br>Development Plan</div>
<ul class="plan"><li><i>01</i><span>Sandhill (Lease)<small>Q2-22</small></span></li><li><i>02</i><span>Falcon (PSA)<small>Q3-22</small></span></li><li><i>03</i><span>Pueblo<small>Target - Q4-24</small></span></li></ul>
<div class="pg">16</div></div>

<!-- Row 9 -->
<div class="slide c1" style="top:3469px">
<div class="mark">RWP</div>
<div class="ph" role="img" aria-label="Map of Florida development sites" style="left:0;top:0;width:290px;height:307px;background:linear-gradient(160deg,#e6ebe2,#cdd8cc 55%,#a9c6da)"></div>
<div class="h2" style="left:320px;top:60px">Florida<br>Development Plan</div>
<ul class="plan" style="top:160px"><li><i>01</i><span>Fleming Island<small>Under Review</small></span></li><li><i>02</i><span>Durbin Creek – LOI<small>Target Q3-23</small></span></li><li><i>03</i><span>Yulee – LOI<small>Target Q3-23</small></span></li></ul>
<div class="pg">17</div></div>

<div class="slide c2" style="top:3469px">
<div class="mark">RWP</div>
<div class="ph" role="img" aria-label="Map of Colorado development sites" style="left:0;top:0;width:300px;height:307px;background:linear-gradient(160deg,#e8ece4,#cfd9cf 60%,#bcc8d3)"></div>
<div class="h2" style="left:320px;top:60px">Colorado<br>Development Plan</div>
<ul class="plan" style="top:160px"><li><i>01</i><span>Sandhill (Lease)<small>Q2-22</small></span></li><li><i>02</i><span>Falcon (PSA)<small>Q3-22</small></span></li><li><i>03</i><span>Pueblo<small>Target - Q4-24</small></span></li></ul>
<div class="pg">18</div></div>

<!-- Row 10 -->
<div class="slide c1" style="top:3797px">
<div class="mark">RWP</div>
<div class="stitle" style="line-height:22px">Lantern Harbor Merger into<br>RWP Double Cheese LLC</div>
<div style="position:absolute;left:70px;top:150px;font:900 40px Roboto,sans-serif;color:var(--ink)">RWP</div>
<div class="sub" style="position:absolute;left:70px;top:205px;font-size:6.5px;color:var(--ink);font-weight:700">Target Transition Date:</div>
<div class="sub" style="position:absolute;left:70px;top:215px;font-size:6px">Monday September 6, 2021</div>
<div class="bbox" style="left:260px;top:96px;width:301px;height:168px;padding:10px 14px">
<div style="display:grid;grid-template-columns:90px 1fr;row-gap:14px;align-items:center">
<div><div class="k" style="background:#fff;color:var(--blue);padding:1px 4px">Senior Debt Refi</div><div class="v">$3.93M</div></div><div class="k">Floor of 3.00%<br>5 yr fixed (25bps + 5yr treasury)</div>
<div><div class="k" style="background:#fff;color:var(--blue);padding:1px 4px">Development Line</div><div class="v">$800K</div></div><div class="k">Converts to above structure</div>
<div><div class="k" style="background:#fff;color:var(--blue);padding:1px 4px">Equity Line</div><div class="v">$730K</div></div><div class="k">Converts to above structure</div>
</div></div>
<div class="pg">19</div></div>

<div class="slide c2" style="top:3797px">
<div class="ph" role="img" aria-label="Regional map showing target territory" style="left:0;top:0;width:320px;height:307px;background:linear-gradient(160deg,#eef1ec,#d8e0d8);opacity:.85"></div>
<div class="h2" style="left:330px;top:78px">Opportunities</div>
<div style="position:absolute;left:350px;top:112px;font:700 12px Roboto,sans-serif;color:var(--red)">Bramble's</div>
<div class="bbox" style="left:260px;top:150px;width:301px;height:100px;padding:12px 18px;display:grid;grid-template-columns:60px 1fr 1fr;row-gap:10px">
<div style="font-weight:700">M&amp;A Target</div>
<div><div class="k">To acquire a franchise group with</div><div class="v">21 <span style="font-size:6px;font-weight:400">Operating Units</span></div></div>
<div><div class="k">Development territory</div><div class="v">50+ <span style="font-size:6px;font-weight:400">Units</span></div></div>
<div></div>
<div><div class="k">Target Price</div><div class="v">$20M - $25M</div></div>
<div><div class="k">Ebitda Range</div><div class="v">$2M</div></div></div>
<div class="pg">20</div></div>

<!-- Row 11 -->
<div class="slide c1" style="top:4129px">
<div class="mark">RWP</div>
<div class="stitle">Calendar</div>
<div class="ph" role="img" aria-label="Illustration of a frozen custard sundae" style="left:28px;top:90px;width:70px;height:120px;background:linear-gradient(180deg,#f3e6d6,#d8b48c 60%,#b3202c);border-radius:30px 30px 8px 8px"></div>
<svg style="position:absolute;left:110px;top:120px" width="430" height="60"><rect x="0" y="22" width="425" height="16" rx="8" fill="#1b8cb8"/><rect x="40" y="22" width="230" height="16" fill="#9fb3c1"/>
<g fill="#fff" stroke="#1b8cb8" stroke-width="2"><circle cx="20" cy="30" r="13"/><circle cx="110" cy="30" r="13"/><circle cx="205" cy="30" r="13"/><circle cx="300" cy="30" r="13"/></g>
<g fill="#1b8cb8"><rect x="14" y="25" width="12" height="10" rx="1"/><rect x="104" y="25" width="12" height="10" rx="1"/><rect x="199" y="25" width="12" height="10" rx="1"/><rect x="294" y="25" width="12" height="10" rx="1"/></g></svg>
<div class="list" style="position:absolute;left:160px;top:84px;line-height:9px;font-size:5.5px">End of October<br><b>Tax Planning Meeting</b></div>
<div class="list" style="position:absolute;left:340px;top:84px;line-height:9px;font-size:5.5px">October 20th, 2021<br><b>Quarter 3 Meeting Date</b><br>Qtr 3 ends 9/30/21</div>
<div class="list" style="position:absolute;left:250px;top:188px;line-height:9px;font-size:5.5px">End of November<br><b>2022 Budgeting</b></div>
<div class="list" style="position:absolute;left:425px;top:188px;line-height:9px;font-size:5.5px">October 6, 2021<br><b style="color:var(--blue)">RWP Double Cheese<br>Internal Announcement</b></div>
<div class="pg">21</div></div>

<div class="slide c2" style="top:4129px">
<div class="ph" role="img" aria-label="Burger restaurant exterior at dusk with lit red sign" style="left:0;top:0;width:561px;height:314px;background:linear-gradient(180deg,#4a4f5c,#7b5a53 45%,#b3202c 60%,#2b2b30)"></div>
<div style="position:absolute;left:0;right:0;bottom:0;height:80px;background:var(--blue)"></div>
<div style="position:absolute;left:40px;bottom:30px;font:900 14px Roboto,sans-serif;color:#fff">RWP</div>
<div style="position:absolute;left:120px;bottom:24px;font:500 28px Roboto,sans-serif;color:#fff">Questions?</div>
</div>

</div></body></html>
```